Packaging Design Project - Organic Baby Skin Care

This project is to re-design our current organic baby skin care range labels. See here:

http://www.velvetmeadow.com.au/Baby-Care

The common complaint is that the pink is too girly for boys. For this reason I am not sure if I should keep the "Velvet Meadow Baby" Logo as it is a bit girly looking as well. So open to your ideas.

The size of the label will be approx 90 w x 70 h mm

Here is one range I like that is already similar to what I am already doing with the polka dots but in different pastels: http://www.tinkettlestore.com/baby-skincare.html

Also another idea for a concept here with a beige/vintage look background: http://www.barnloftstore.com/wee_lark_naturals/wee_lark_naturals_creamy_body_lotion-c502817p730461.html

Lastly, I also like these fun colourful, child like graphics of this range:

http://www.tinyfernnaturals.co.uk/brands/hush-drowsy-bean/

The range consists of:

Soothing Tot Salve in a white tube
Bubbly Fresh Tot Wash in a white 250ml bottle
Nana and Pip Rubdown Oil in a white 100ml bottle
Quiet Night Settling Spray in a white 100ml bottle
Oat Cream Bar in a cardboard box

See packaging attached.

I will be presenting all the designs to a group of mother's for market research so they will be making the final decision - seeing they are the ones who will ultimately buy the product.

That is why I am open to a wide range of styles for this project.

Looking forward to seeing your work!

Any questions, let me know!
Updates

Hello Designers!

I have posted an update to include more information in the brief and also the AI logo file which shows the current packaging. Also images of the bottles of the current range. The bottles will be white boston round bottles not the tall boston as I am currently using.

many thanks

Rosalind

Hello Designers

Just wanted to get an update on how you are going with your design submissions?

The deadline is this Saturday and we have received very few designs.

I await your reply.

thanks
Rosalind

Reason: The deadline is drawing near and have not received enough designs. Please submit your designs as soon as you can. Many thanks Rosalind Velvet Meadow

Target Market(s)

Mothers 25 - 40

Industry/Entity Type

Market Research

Requirements
Must have
• Organic/Natural feel, Stylish, Elegant, Gender Neutral to suit both sexes
Nice to have
• Vintage feel

```html
<!DOCTYPE html>
<html lang="en">
<head>
<meta charset="utf-8">
<title>Velvet Meadow Baby – Label Range</title>
<link rel="stylesheet" href="https://fonts.googleapis.com/css2?family=Oleo+Script:wght@400;700&family=Arimo:wght@400&display=swap">
<style>
  :root {
    --canvas: #f4f4f6;
    --mint: #a6dccb;
    --mint-deep: #8fd0bc;
    --lavender: #e4dcec;
    --lavender-light: #f1ecf5;
    --plum: #8e6497;
    --plum-soft: #a88bb0;
    --cartouche: #ffffff;
    --band-text: #ffffff;
    --sun: #f3d64a;
    --violet: #a57fb0;
    --sky: #7ec8dc;
    --leaf: #a9c455;
    --rose: #e58cc0;
  }
  * { box-sizing: border-box; margin: 0; padding: 0; }
  html, body { width: 1200px; height: 808px; overflow: hidden; }
  body { background: var(--canvas); font-family: "Arimo", Arial, sans-serif; }

  .range {
    position: relative;
    width: 1200px; height: 808px;
    display: flex; align-items: center; justify-content: center; gap: 24px;
  }

  .label {
    position: relative;
    width: 210px; height: 440px;
    display: flex; flex-direction: column;
    box-shadow: 0 2px 10px rgba(120, 100, 140, .15);
  }
  .label__band-top { height: 30px; background: var(--mint); border-bottom: 3px solid var(--mint-deep); }
  .label__field {
    flex: 1; position: relative;
    display: flex; align-items: center; justify-content: center;
  }
  .label__rays {
    position: absolute; inset: 0;
    background: radial-gradient(circle at 50% 45%, var(--lavender-light) 0%, var(--lavender) 70%);
  }
  .label__band-bottom {
    height: 62px; background: var(--mint); border-top: 3px solid var(--mint-deep);
    color: var(--band-text); font-size: 12px; line-height: 1.3;
    display: flex; flex-direction: column; align-items: center; justify-content: center; text-align: center;
  }

  .cartouche {
    position: relative; width: 172px; height: 292px;
    display: flex; flex-direction: column; align-items: center;
    padding: 26px 14px 18px; text-align: center;
  }
  .cartouche__frame { position: absolute; inset: 0; width: 100%; height: 100%; }
  .cartouche > *:not(.cartouche__frame) { position: relative; }

  .brand {
    display: flex; align-items: center; gap: 6px;
    font-family: "Oleo Script", cursive; font-weight: 400;
    font-size: 13px; color: var(--plum-soft); margin-bottom: 22px;
  }
  .brand__dot { width: 14px; height: 14px; border-radius: 50%; flex: none; }

  .product-name {
    font-family: "Oleo Script", cursive; font-weight: 700;
    font-size: 20px; line-height: 1.15; color: var(--plum);
  }
  .product-french {
    font-family: "Oleo Script", cursive; font-weight: 400;
    font-size: 12.5px; line-height: 1.2; color: var(--plum); margin-top: 12px;
  }
  .product-size { font-size: 12px; color: var(--plum-soft); margin-top: auto; }

  .label--soap .label__field { justify-content: flex-end; padding-right: 19px; }
  .side-panel {
    position: absolute; left: 0; top: 0; bottom: 0; width: 0;
  }
  .certificates {
    position: absolute; left: 4px; top: 40px; bottom: 40px;
    display: flex; flex-direction: column; justify-content: space-around;
  }
  .certificate { width: 22px; height: 22px; border-radius: 50%; border: 2px solid var(--cartouche); }
</style>
</head>
<body>
<main class="range">

  <section class="label label--balm">
    <div class="label__band-top"></div>
    <div class="label__field">
      <div class="label__rays" role="img" aria-label="Soft lavender sunburst rays behind the frame"></div>
      <div class="cartouche">
        <svg class="cartouche__frame" viewBox="0 0 172 292" preserveAspectRatio="none" aria-hidden="true"><path d="M22,2 H150 A20,20 0 0 0 170,22 V270 A20,20 0 0 0 150,290 H22 A20,20 0 0 0 2,270 V22 A20,20 0 0 0 22,2 Z" fill="var(--cartouche)" stroke="var(--plum)" stroke-width="2.5"/></svg>
        <div class="brand"><span class="brand__dot" style="background:var(--sun)"></span>Velvet Meadow Baby</div>
        <h2 class="product-name">Soothing Tot<br>Salve</h2>
        <p class="product-french">Baume Curatif<br>Pour Bébé</p>
        <p class="product-size">℮ 100 g &nbsp; 3.5 fl oz.</p>
      </div>
    </div>
    <div class="label__band-bottom"><span>Organic Herbal Blend</span><span>Sulphate &amp; Paraben Free</span></div>
  </section>

  <section class="label label--soap">
    <div class="label__band-top"></div>
    <div class="label__field">
      <div class="label__rays" role="img" aria-label="Soft lavender sunburst rays behind the frame"></div>
      <div class="certificates"><span class="certificate"></span><span class="certificate"></span><span class="certificate"></span></div>
      <div class="cartouche">
        <svg class="cartouche__frame" viewBox="0 0 172 292" preserveAspectRatio="none" aria-hidden="true"><path d="M22,2 H150 A20,20 0 0 0 170,22 V270 A20,20 0 0 0 150,290 H22 A20,20 0 0 0 2,270 V22 A20,20 0 0 0 22,2 Z" fill="var(--cartouche)" stroke="var(--plum)" stroke-width="2.5"/></svg>
        <div class="brand"><span class="brand__dot" style="background:var(--violet)"></span>Velvet Meadow Baby</div>
        <h2 class="product-name">Organic<br>Oat Cream<br>Bar</h2>
        <p class="product-size">100 g &nbsp; 3.5 fl oz.</p>
      </div>
    </div>
    <div class="label__band-bottom"><span>Contains certified organic ingredients</span><span>fragrance free</span></div>
  </section>

  <section class="label label--wash">
    <div class="label__band-top"></div>
    <div class="label__field">
      <div class="label__rays" role="img" aria-label="Soft lavender sunburst rays behind the frame"></div>
      <div class="cartouche">
        <svg class="cartouche__frame" viewBox="0 0 172 292" preserveAspectRatio="none" aria-hidden="true"><path d="M22,2 H150 A20,20 0 0 0 170,22 V270 A20,20 0 0 0 150,290 H22 A20,20 0 0 0 2,270 V22 A20,20 0 0 0 22,2 Z" fill="var(--cartouche)" stroke="var(--plum)" stroke-width="2.5"/></svg>
        <div class="brand"><span class="brand__dot" style="background:var(--sky)"></span>Velvet Meadow Baby</div>
        <h2 class="product-name">Bubbly Fresh<br>Tot Wash</h2>
        <p class="product-french">Savon Pour<br>Le Bain De Bébé</p>
        <p class="product-size">℮ 250 g &nbsp; 8.5 fl oz.</p>
      </div>
    </div>
    <div class="label__band-bottom"><span>Organic Herbal Blend</span><span>Sulphate &amp; Paraben Free</span></div>
  </section>

  <section class="label label--oil">
    <div class="label__band-top"></div>
    <div class="label__field">
      <div class="label__rays" role="img" aria-label="Soft lavender sunburst rays behind the frame"></div>
      <div class="cartouche">
        <svg class="cartouche__frame" viewBox="0 0 172 292" preserveAspectRatio="none" aria-hidden="true"><path d="M22,2 H150 A20,20 0 0 0 170,22 V270 A20,20 0 0 0 150,290 H22 A20,20 0 0 0 2,270 V22 A20,20 0 0 0 22,2 Z" fill="var(--cartouche)" stroke="var(--plum)" stroke-width="2.5"/></svg>
        <div class="brand"><span class="brand__dot" style="background:var(--leaf)"></span>Velvet Meadow Baby</div>
        <h2 class="product-name">Nana &amp; Pip<br>Rubdown Oil</h2>
        <p class="product-french">Huile de Massage<br>Pour Maman et Bébé</p>
        <p class="product-size">℮ 100 g &nbsp; 3.5 fl oz.</p>
      </div>
    </div>
    <div class="label__band-bottom"><span>Organic Herbal Blend</span><span>Sulphate &amp; Paraben Free</span></div>
  </section>

  <section class="label label--mist">
    <div class="label__band-top"></div>
    <div class="label__field">
      <div class="label__rays" role="img" aria-label="Soft lavender sunburst rays behind the frame"></div>
      <div class="cartouche">
        <svg class="cartouche__frame" viewBox="0 0 172 292" preserveAspectRatio="none" aria-hidden="true"><path d="M22,2 H150 A20,20 0 0 0 170,22 V270 A20,20 0 0 0 150,290 H22 A20,20 0 0 0 2,270 V22 A20,20 0 0 0 22,2 Z" fill="var(--cartouche)" stroke="var(--plum)" stroke-width="2.5"/></svg>
        <div class="brand"><span class="brand__dot" style="background:var(--rose)"></span>Velvet Meadow Baby</div>
        <h2 class="product-name">Quiet Night<br>Settling Spray</h2>
        <p class="product-french">Huile de Massage<br>Pour Maman et Bébé</p>
        <p class="product-size">℮ 100 g &nbsp; 3.5 fl oz.</p>
      </div>
    </div>
    <div class="label__band-bottom"><span>Organic Herbal Blend</span><span>Sulphate &amp; Paraben Free</span></div>
  </section>

</main>
</body>
</html>
```